Simple design for eCommerce retailer of Custom Cut Mirror Frames

We need a fresh design for our eCommerce store. Currently, we need a design for each page on the existing site.

Here is the site as it stands right now: glassvela.com

Here is a competitor site that we like. The owner really likes the block look for the home page: framorly.com

Here is a video we would like to feature: https://videohost.example/v/Kp7rTq2LmXa

Here is the color palate, emphasis on the green and purple: https://palettes.example/quiet-bay-theme-48271953/?showPublished=true

Here is an example of a landing page we are currently using: https://glassvela.com/lander-10-off-install/

Font for the site should be the google font Lato

Home page should include the following sections/blocks:

How it works
Shop now
Testimonials
Featured Products
Before and After Gallery
Updates

My team has been slow getting back to me with feedback. I'm pushing them to speed their process up.

Target Market(s)

Women, Ages 35-65+

Number of Pages Required

5+ page

Font styles to use
Sans Serif

Requirements
Must have
• -Before and after gallery
• -Star ratings
• -eCommerce look and feel
• -Info about being able to order free samples
• -Language from the checkmarks on the landing page
• -sleek product page
• -home page should be have a very modern design feel
Should not have
• Product Prices...the user has to use the calculator to determine the price of their purchase.
• Sliders

```html
<!DOCTYPE html>
<html lang="en">
<head>
<meta charset="utf-8">
<title>GlassVela – Custom Mirror Frames</title>
<link href="https://fonts.googleapis.com/css2?family=Lato:ital,wght@0,400;0,700;1,400&display=swap" rel="stylesheet">
<style>
:root{
  --purple:#c39bca;
  --purple-light:#cfadd4;
  --teal:#8fbfbf;
  --pink:#d49ad4;
  --ink:#2b2b2b;
  --text:#555;
  --line:#e3e3e3;
  --soft:#f4f4f4;
  --star:#f5c518;
  --white:#fff;
}
*{box-sizing:border-box;margin:0;padding:0}
html,body{width:1200px;height:4562px;overflow:hidden}
body{position:relative;font-family:'Lato',sans-serif;color:var(--text);background:var(--white)}
.abs{position:absolute}
.topbar{left:0;top:0;width:1200px;height:40px;background:var(--purple);color:var(--white);font-size:13px;display:flex;justify-content:space-between;align-items:center;padding:0 80px}
.phone{left:76px;top:88px;font-size:15px;display:flex;align-items:center;gap:10px}
.brand{left:0;width:1200px;top:76px;display:flex;justify-content:center;align-items:center;gap:10px}
.brand-mark{width:26px;height:26px;background:var(--purple)}
.brand-name{font-size:30px;font-weight:700;color:var(--ink)}
.header-icons{right:90px;top:86px;display:flex;gap:22px;align-items:center}
.nav{left:0;top:156px;width:1200px;height:51px;border-top:1px solid var(--line);border-bottom:1px solid var(--line);display:flex;justify-content:center;align-items:center;font-size:13px;color:#444}
.nav a{padding:0 28px;border-right:1px solid var(--line);text-decoration:none;color:inherit}
.nav a:last-child{border-right:0}
.nav a.active{color:var(--pink)}
.hero{left:0;top:207px;width:1200px;height:563px;background:linear-gradient(90deg,#cfd1d4 0%,#bfc2c6 60%,#d9dadc 100%)}
.section-title{left:0;width:1200px;text-align:center;font-size:40px;font-weight:700;color:var(--ink)}
.step{width:240px;text-align:center;font-size:17px;color:#666}
.step-circle{width:104px;height:104px;border:2px solid #ccc;border-radius:50%;margin:0 auto 36px;position:relative;display:flex;align-items:center;justify-content:center}
.step-num{position:absolute;right:-6px;top:0;width:28px;height:28px;border-radius:50%;background:var(--teal);color:#fff;font-size:13px;display:flex;align-items:center;justify-content:center}
.band-soft{left:0;width:1200px;background:var(--soft)}
.band-purple{left:0;width:1200px;background:var(--purple)}
.card{width:240px;background:var(--white);border:1px solid #ddd;text-align:center}
.card .tag{position:absolute;left:14px;top:16px;width:104px;height:40px;border:1px solid #bbb;color:var(--teal);font-size:15px;display:flex;align-items:center;justify-content:center}
.card .frame{position:absolute;left:36px;top:110px;width:168px;height:80px}
.card .photo{position:absolute;left:15px;top:16px;width:208px;height:156px}
.stars{color:var(--star);font-size:20px;letter-spacing:3px}
.card .name{font-size:18px;color:#333}
.card .sub{font-size:13px;color:#666}
.btn{display:flex;align-items:center;justify-content:center;background:var(--teal);color:#fff;font-size:15px;font-weight:700}
.card .btn{position:absolute;left:15px;width:208px;height:40px}
.testi-panel{left:439px;top:1913px;width:322px;height:312px;background:var(--purple-light)}
.quote{left:0;width:1200px;text-align:center;color:#fff;font-style:italic;font-size:17px;line-height:29px}
.dots{display:flex;gap:6px;justify-content:center;left:0;width:1200px}
.dot{width:12px;height:12px;border-radius:50%}
.gallery-img{top:3039px;height:271px}
.footer-col h4{font-size:19px;font-weight:400;color:#333;margin-bottom:20px}
.footer-col li{list-style:none;font-size:13px;color:#555;margin-bottom:23px;display:flex;align-items:center;gap:14px}
.footer-col li::before{content:"";width:9px;height:9px;border-radius:50%;background:var(--teal)}
.copyright{left:0;top:4496px;width:1200px;height:66px;background:var(--purple);color:#fff;font-size:13px;display:flex;align-items:center;justify-content:center}
</style>
</head>
<body>

<div class="abs topbar"><span>In Bayview, or North Crest County? Free In-home Consultation</span><span>Get up to 7 Samples FREE! Use code: freesample at checkout.</span></div>

<div class="abs phone">
  <svg width="18" height="18" viewBox="0 0 24 24"><path d="M6.6 10.8a15 15 0 0 0 6.6 6.6l2.2-2.2c.3-.3.7-.4 1-.2 1.1.4 2.3.6 3.6.6.6 0 1 .4 1 1V20c0 .6-.4 1-1 1A17 17 0 0 1 3 4c0-.6.4-1 1-1h3.5c.6 0 1 .4 1 1 0 1.3.2 2.5.6 3.6.1.3 0 .7-.2 1z" fill="#333"/></svg>
  (555) 014-2276
</div>
<div class="abs brand"><span class="brand-mark"></span><span class="brand-name">GlassVela</span></div>
<div class="abs header-icons">
  <svg width="20" height="20" viewBox="0 0 24 24"><circle cx="12" cy="7" r="5" fill="#222"/><path d="M2 22c0-6 4-9 10-9s10 3 10 9z" fill="#222"/></svg>
  <span style="width:1px;height:22px;background:#ccc"></span>
  <svg width="22" height="20" viewBox="0 0 24 22"><path d="M1 8h22l-3 12H4z" fill="#222"/><path d="M7 8l5-6 5 6" stroke="#222" stroke-width="2" fill="none"/></svg>
</div>

<nav class="abs nav">
  <a class="active">HOME</a><a>SHOP MIRROR FRAMES</a><a>CUTOM FRAMED MIRRORS</a><a>HOW IT WORKS</a><a>BEFORE &amp; AFTER GALLERY</a>
</nav>

<div class="abs hero" role="img" aria-label="Bathroom with a framed mirror above twin vessel sinks, with a pinned photo inset and the handwritten line Frame any Mirror in Your House"></div>

<h2 class="abs section-title" style="top:815px">How it works</h2>
<div class="abs step" style="left:119px;top:903px"><div class="step-circle"><span class="step-num">1</span>
  <svg width="36" height="36" viewBox="0 0 36 36"><path d="M4 4v28h28z M10 20v6h6z" fill="none" stroke="#444" stroke-width="1.6"/><path d="M8 4l24 24" stroke="#444" stroke-width="1.2"/></svg></div>Measure Your Mirror</div>
<div class="abs step" style="left:480px;top:903px"><div class="step-circle"><span class="step-num">2</span>
  <svg width="38" height="32" viewBox="0 0 38 32"><rect x="2" y="2" width="34" height="28" fill="none" stroke="#444" stroke-width="1.6"/><rect x="7" y="7" width="24" height="18" fill="none" stroke="#444" stroke-width="1.2"/><path d="M12 20l6-6M18 20l6-6" stroke="#444"/></svg></div>Choose A Frame</div>
<div class="abs step" style="left:841px;top:903px"><div class="step-circle"><span class="step-num">3</span>
  <svg width="36" height="36" viewBox="0 0 36 36"><circle cx="18" cy="18" r="11" fill="none" stroke="#444" stroke-width="5" stroke-dasharray="4 3.2"/><circle cx="18" cy="18" r="9" fill="none" stroke="#444" stroke-width="1.6"/><circle cx="18" cy="18" r="4" fill="none" stroke="#444" stroke-width="1.6"/></svg></div>Easy No Tools Installation</div>
<svg class="abs" style="left:336px;top:940px" width="170" height="30"><path d="M2 24 Q80 2 160 14" stroke="#bbb" stroke-dasharray="3 3" fill="none"/><path d="M154 9l7 5-8 3" stroke="#bbb" fill="none"/></svg>
<svg class="abs" style="left:697px;top:940px" width="170" height="30"><path d="M2 24 Q80 2 160 14" stroke="#bbb" stroke-dasharray="3 3" fill="none"/><path d="M154 9l7 5-8 3" stroke="#bbb" fill="none"/></svg>

<div class="abs band-soft" style="top:1124px;height:625px"></div>
<h2 class="abs section-title" style="top:1170px">Shop now</h2>

<div class="abs card" style="left:76px;top:1248px;height:416px"><span class="tag">NEW</span><div class="frame" role="img" aria-label="Silver frame corner sample" style="background:linear-gradient(135deg,#b8ad8c,#8f8466)"></div>
  <div class="abs" style="left:0;width:100%;top:232px"><div class="stars">★★★★★</div><div class="name" style="margin-top:10px">Harbor Silver</div><div class="sub" style="margin-top:12px">Modern Look</div></div><div class="btn" style="top:347px">BUY NOW</div></div>
<div class="abs card" style="left:347px;top:1248px;height:416px"><span class="tag">NEW</span><div class="frame" role="img" aria-label="Bronze frame corner sample" style="background:linear-gradient(135deg,#6b4a2c,#2e1e12)"></div>
  <div class="abs" style="left:0;width:100%;top:232px"><div class="stars">★★★★★</div><div class="name" style="margin-top:10px">Seabrook Bronze</div><div class="sub" style="margin-top:12px">Elegant Look</div></div><div class="btn" style="top:347px">BUY NOW</div></div>
<div class="abs card" style="left:614px;top:1248px;height:416px"><span class="tag">NEW</span><div class="frame" role="img" aria-label="Black and silver frame corner sample" style="background:linear-gradient(135deg,#4a4440,#1c1a19)"></div>
  <div class="abs" style="left:0;width:100%;top:232px"><div class="stars">★★★★★</div><div class="name" style="margin-top:10px">Seabrook Black Silver</div><div class="sub" style="margin-top:12px">Versatile Look</div></div><div class="btn" style="top:347px">BUY NOW</div></div>
<div class="abs card" style="left:882px;top:1248px;height:416px"><span class="tag">NEW</span><div class="frame" role="img" aria-label="Espresso frame corner sample" style="background:linear-gradient(135deg,#8a5a2c,#3b2412)"></div>
  <div class="abs" style="left:0;width:100%;top:232px"><div class="stars">★★★★★</div><div class="name" style="margin-top:10px">Linden Espresso</div><div class="sub" style="margin-top:12px">Modern Look</div></div><div class="btn" style="top:347px">BUY NOW</div></div>

<div class="abs band-purple" style="top:1749px;height:582px"></div>
<h2 class="abs section-title" style="top:1795px;color:#fff">Testimonials</h2>
<div class="abs testi-panel"></div>
<div class="abs" role="img" aria-label="Customer portrait" style="left:558px;top:1871px;width:84px;height:84px;border-radius:50%;border:3px solid #fff;background:linear-gradient(#d9c2b4,#8a6e62)"></div>
<div class="abs" style="left:0;width:1200px;top:1980px;text-align:center;color:#fff;font-size:44px;font-weight:700;line-height:1">&ldquo;</div>
<p class="abs quote" style="top:2032px">Great product and great service! Adding frames to our mirrors made all the difference in how<br>the master bath looks. You can't beat GlassVela for the money!</p>
<div class="abs stars" style="left:0;width:1200px;top:2118px;text-align:center;font-size:22px">★★★★★</div>
<div class="abs" style="left:0;width:1200px;top:2156px;text-align:center;color:#f1e6f3;font-size:17px">Marla T., Alder Cove, Ca</div>
<div class="abs dots" style="top:2253px"><span class="dot" style="background:#fff"></span><span class="dot" style="background:#dcc6e0"></span><span class="dot" style="background:#dcc6e0"></span></div>

<h2 class="abs section-title" style="top:2378px">Featured Products</h2>
<div class="abs card" style="left:76px;top:2452px;height:373px"><div class="photo" role="img" aria-label="Silver framed mirror close-up" style="background:linear-gradient(135deg,#8c8470 0 18%,#e6ece9 18%)"></div>
  <div class="abs" style="left:0;width:100%;top:194px"><div class="stars">★★★★★</div><div class="name" style="margin-top:10px">Harbor Silver</div><div class="sub" style="margin-top:12px">Modern Look</div></div><div class="btn" style="top:304px">BUY NOW</div></div>
<div class="abs card" style="left:347px;top:2452px;height:373px"><div class="photo" role="img" aria-label="Bronze framed mirror close-up" style="background:linear-gradient(135deg,#7a4b2a 0 18%,#f5f5f5 18%)"></div>
  <div class="abs" style="left:0;width:100%;top:194px"><div class="stars">★★★★★</div><div class="name" style="margin-top:10px">Seabrook Bronze</div><div class="sub" style="margin-top:12px">Elegant Look</div></div><div class="btn" style="top:304px">BUY NOW</div></div>
<div class="abs card" style="left:614px;top:2452px;height:373px"><div class="photo" role="img" aria-label="Black silver framed mirror close-up" style="background:linear-gradient(135deg,#dad8d2 0 20%,#e9ebeb 20%)"></div>
  <div class="abs" style="left:0;width:100%;top:194px"><div class="stars">★★★★★</div><div class="name" style="margin-top:10px">Seabrook Black Silver</div><div class="sub" style="margin-top:12px">Versatile Look</div></div><div class="btn" style="top:304px">BUY NOW</div></div>
<div class="abs card" style="left:882px;top:2452px;height:373px"><div class="photo" role="img" aria-label="Espresso framed mirror close-up" style="background:linear-gradient(135deg,#222 0 16%,#e8eaea 16%)"></div>
  <div class="abs" style="left:0;width:100%;top:194px"><div class="stars">★★★★★</div><div class="name" style="margin-top:10px">Linden Espresso</div><div class="sub" style="margin-top:12px">Modern Look</div></div><div class="btn" style="top:304px">BUY NOW</div></div>

<div class="abs band-soft" style="top:2912px;height:511px"></div>
<h2 class="abs section-title" style="top:2962px">Before and After Gallery</h2>
<div class="abs gallery-img" role="img" aria-label="Bathroom before: unframed mirror over dark granite vanity" style="left:76px;width:276px;background:linear-gradient(90deg,#6b3e26,#d9c3a8 50%,#5a3320)"></div>
<div class="abs gallery-img" role="img" aria-label="Bathroom after: dark framed mirror over granite vanity" style="left:359px;width:218px;background:linear-gradient(90deg,#4a2a1a,#c9b39a 50%,#3a2014)"></div>
<div class="abs gallery-img" role="img" aria-label="Bathroom before: plain mirror over grey marble vanity" style="left:623px;width:243px;background:linear-gradient(#c7cdca,#a8adb0 70%,#586880)"></div>
<div class="abs gallery-img" role="img" aria-label="Bathroom after: framed mirror over grey marble vanity" style="left:869px;width:253px;background:linear-gradient(#c3c8c6,#8f9496 70%,#536278)"></div>
<div class="abs dots" style="top:3352px"><span class="dot" style="background:var(--teal)"></span><span class="dot" style="border:1.5px solid var(--teal)"></span><span class="dot" style="border:1.5px solid var(--teal)"></span><span class="dot" style="border:1.5px solid var(--teal)"></span></div>

<div class="abs band-purple" style="top:3423px;height:667px"></div>
<h2 class="abs section-title" style="top:3480px;color:#fff;font-size:34px">100% Satisfaction Guarantee!</h2>
<p class="abs" style="left:0;width:1200px;top:3541px;text-align:center;color:#fff;font-size:17px">Unsure? – Don't Worry, We Will Walk You Through Every Step Of The Process.</p>
<div class="abs btn" style="left:506px;top:3593px;width:188px;height:50px;font-weight:400">SHOP NOW</div>
<h2 class="abs section-title" style="top:3696px;color:#fff;font-size:34px">See How Easy It Is</h2>
<p class="abs" style="left:0;width:1200px;top:3756px;text-align:center;color:#fff;font-size:17px">to install our custom made frames</p>
<div class="abs" role="img" aria-label="Installation video still: presenter standing in a kitchen" style="left:267px;top:3818px;width:666px;height:377px;background:linear-gradient(90deg,#5a2e1a,#7a4a34 30%,#3a2fa0 50%,#6b4030 70%,#8a8a8c)"></div>
<div class="abs" style="left:567px;top:3973px;width:66px;height:66px;border-radius:50%;background:var(--teal);display:flex;align-items:center;justify-content:center"><svg width="22" height="24" viewBox="0 0 22 24"><path d="M4 3l15 9-15 9z" fill="none" stroke="#fff" stroke-width="2"/></svg></div>

<div class="abs" style="left:76px;top:4292px;display:flex;align-items:center;gap:10px"><span class="brand-mark"></span><span style="font-size:28px;font-weight:700;color:var(--ink)">GlassVela</span></div>
<div class="abs" style="left:76px;top:4378px;display:flex;align-items:center;gap:14px;font-size:21px;color:#222">
  <svg width="22" height="22" viewBox="0 0 24 24"><path d="M6.6 10.8a15 15 0 0 0 6.6 6.6l2.2-2.2c.3-.3.7-.4 1-.2 1.1.4 2.3.6 3.6.6.6 0 1 .4 1 1V20c0 .6-.4 1-1 1A17 17 0 0 1 3 4c0-.6.4-1 1-1h3.5c.6 0 1 .4 1 1 0 1.3.2 2.5.6 3.6.1.3 0 .7-.2 1z" fill="var(--teal)"/></svg>(555) 014-2276</div>
<div class="abs footer-col" style="left:349px;top:4259px"><h4>Company Info</h4><ul><li>GlassVela.com</li><li>About Us</li><li>Privacy Policy</li><li>Terms and Conditions</li></ul></div>
<div class="abs footer-col" style="left:616px;top:4259px"><h4>Policies &amp; Product Info</h4><ul><li>Our Guarantee</li><li>Shipping</li><li>Product Care</li><li>Return Policy</li></ul></div>
<div class="abs footer-col" style="left:885px;top:4259px"><h4>Services &amp; Support</h4><ul><li>FAQ</li><li>Customer Support</li><li>Contact Us</li></ul></div>

<div class="abs copyright">©GlassVela. 2018 - All Rights Reserved.</div>

</body>
</html>
```